New Business Card for Casual Beachfront Cafe

Quirky Beachfront Cafe at Moana, South Australia needs a DOUBLE SIDED business card to print on PressLoom.

Target Market(s)

Business Cards sit on the counter for Guests to take with them. Please view our website www.saltwhistlekitchen.com.au to get a feel for the Cafe. You may also view our Instagram at @saltwhistlekitchen

Industry/Entity Type

Cafe / Restaurant

Contact Information for Business Card

Information equivalent to: Breakfast, Lunch, Dinner, Coffee, Takeaway / 87 Tidewater Parade Moana SA 5169 / Menu & Opening Hours: www.saltwhistlekitchen.com.au / ph (08) 8591 2736

Requirements
Must have
• Information equivalent to: Breakfast, Lunch, Dinner, Coffee, Takeaway / 87 Tidewater Parade Moana SA 5169 / Menu & Opening Hours: www.saltwhistlekitchen.com.au / ph (08) 8591 2736
Nice to have
• Potentially some of our trademark colours (Cafe can be searched via Trovix)
Should not have
• Must NOT have image of the building. May have the logo provided on one side but not necessarily, depending on how you wish to design the card

```html
<!DOCTYPE html>
<html lang="en">
<head>
<meta charset="utf-8">
<title>Salt Whistle Kitchen – Business Card</title>
<link rel="stylesheet" href="https://fonts.googleapis.com/css2?family=Montserrat:wght@400;500;700;800&display=swap">
<style>
  :root {
    --backdrop: #e9e6e1;
    --card: #ffffff;
    --brand-blue: #1c4480;
    --rust: #b5582a;
    --ink: #222222;
  }
  * { box-sizing: border-box; margin: 0; padding: 0; }
  html, body {
    width: 900px; height: 1200px; overflow: hidden;
    background: var(--backdrop);
    font-family: "Montserrat", sans-serif;
    color: var(--ink);
  }
  .canvas { position: relative; width: 900px; height: 1200px; }
  .card {
    position: absolute; left: 78px; width: 744px; height: 442px;
    background: var(--card); border-radius: 36px;
    box-shadow: 0 4px 10px rgba(0,0,0,0.18);
  }
  .card--front { top: 130px; }
  .card--back { top: 637px; }

  .brand-name {
    position: absolute; color: var(--brand-blue);
    font-weight: 800; text-transform: uppercase; text-align: center;
    letter-spacing: 0.5px;
  }
  .card--front .brand-name {
    left: 42px; top: 135px; width: 328px;
    font-size: 36px; line-height: 1.1;
  }
  .card--back .brand-name {
    left: 90px; top: 120px; width: 564px;
    font-size: 66px; line-height: 1.1;
  }

  .divider {
    position: absolute; left: 396px; top: 92px;
    width: 2px; height: 260px; background: var(--rust);
  }
  .details { position: absolute; left: 422px; top: 92px; }
  .person-name {
    color: var(--rust); font-weight: 700; font-size: 28px; line-height: 36px;
    letter-spacing: 0.5px;
  }
  .person-role { font-size: 18px; font-weight: 500; margin-top: 2px; }
  .contact-list { list-style: none; margin-top: 26px; }
  .contact-list li {
    display: flex; align-items: center; gap: 6px;
    font-size: 18px; line-height: 29px;
  }
  .contact-list svg { width: 17px; height: 17px; flex: none; }
  .address { font-size: 18px; line-height: 29px; margin-top: 24px; }
  .services {
    position: absolute; left: 0; right: 0; top: 380px;
    text-align: center; font-size: 18px;
  }
</style>
</head>
<body>
<main class="canvas">
  <section class="card card--front" aria-label="Card front">
    <p class="brand-name">Salt Whistle Kitchen</p>
    <div class="divider"></div>
    <div class="details">
      <p class="person-name">DANIEL HARTLEY</p>
      <p class="person-role">Managing Director</p>
      <ul class="contact-list">
        <li>
          <svg viewBox="0 0 24 24" aria-hidden="true"><path fill="#b5582a" d="M6.6 10.8a15.1 15.1 0 0 0 6.6 6.6l2.2-2.2c.3-.3.7-.4 1-.2 1.1.4 2.3.6 3.6.6.6 0 1 .4 1 1V20c0 .6-.4 1-1 1C10.6 21 3 13.4 3 4c0-.6.4-1 1-1h3.5c.6 0 1 .4 1 1 0 1.3.2 2.5.6 3.6.1.3 0 .7-.2 1z"/></svg>
          (08) 8591 2736
        </li>
        <li>
          <svg viewBox="0 0 24 24" aria-hidden="true"><rect x="4" y="4" width="16" height="16" rx="2" fill="#b5582a"/></svg>
          @saltwhistlekitchen
        </li>
        <li>
          <svg viewBox="0 0 24 24" aria-hidden="true"><circle cx="12" cy="12" r="8" fill="#b5582a"/></svg>
          www.saltwhistlekitchen.com.au
        </li>
      </ul>
      <p class="address">87 Tidewater Parade<br>Moana SA 5169</p>
    </div>
    <p class="services">Breakfast, Lunch, Dinner, Coffee, Takeaway</p>
  </section>

  <section class="card card--back" aria-label="Card back">
    <p class="brand-name">Salt Whistle Kitchen</p>
  </section>
</main>
</body>
</html>
```